Coffee Shop needs a fresh new menu

Hi,
I would like a new menu to be designed for our coffee shop.
We display our menu on a television screen, so would need it in a file that would allow us to continue to do so -- I have attached a photo so that you can see our current design, and how it is displayed.

I'd like something that is easy to read, if the design could have a "hipster" feel to it -- we are located at a hospital and University.

I have attached a Word file with what we would like on the menu.

Feel free to contact me if you have any questions.

Thanks,
Liv

Just A4 size will be fine, and no need to include menu 1 and menu 2 - I just put them in as an example of what we already have -- they are our printed menu's. Thanks

Hospital

```html
<!DOCTYPE html>
<html lang="en">
<head>
<meta charset="utf-8">
<title>Ward Café Menu</title>
<link rel="stylesheet" href="https://fonts.googleapis.com/css2?family=Roboto+Condensed:wght@400;700&family=Oswald:wght@500;700&family=Kaushan+Script&display=swap">
<style>
:root{
  --bg:#e9e6e1;
  --paper:#f3eee4;
  --paper-warm:#ecdcc0;
  --ink:#2a2623;
  --brown:#7a2a12;
  --red:#c8202c;
  --orange:#e8742a;
  --yellow:#f6cf6a;
  --pale-yellow:#f8dc8c;
}
*{margin:0;padding:0;box-sizing:border-box}
html,body{width:1200px;height:1000px;overflow:hidden;background:var(--bg)}
body{position:relative;font-family:"Roboto Condensed",Arial Narrow,sans-serif;color:var(--ink)}
.card{position:absolute;left:50px;width:1100px;height:440px;overflow:hidden;box-shadow:0 4px 14px rgba(0,0,0,.18)}
.food-card{top:30px;background:linear-gradient(135deg,#f1e2c6,var(--paper-warm))}
.coffee-card{top:520px;background:radial-gradient(circle at 45% 55%,#fffdf9,var(--paper) 70%)}
.photo{position:absolute}
.brand{position:absolute;display:flex;align-items:center;gap:8px;color:var(--red);font-family:"Oswald",sans-serif;font-weight:700;font-size:30px;letter-spacing:1px}
.brand-dot{width:22px;height:22px;border-radius:50%;background:var(--red)}
.hours{position:absolute;font-size:11px;letter-spacing:1px;text-transform:uppercase}
.list{position:absolute;font-size:15px;line-height:22px}
.row{display:flex}
.row span:first-child{width:110px}
.row span{width:80px}
.section-title{font-family:"Oswald",sans-serif;font-weight:700;text-transform:uppercase;letter-spacing:1px}
.light-title{position:absolute;background:var(--pale-yellow);border-radius:8px;padding:2px 12px;font-size:20px}
.food-title{position:absolute;font-size:14px;color:var(--brown);background:var(--pale-yellow);padding:3px 10px}
.food-list{position:absolute;font-size:16px;line-height:26px;color:var(--brown)}
.band{position:absolute;background:var(--yellow)}
.coffee-word{position:absolute;font-family:"Kaushan Script",cursive;color:#fff;font-size:44px}
.small{position:absolute;font-size:11px}
</style>
</head>
<body>

<section class="card food-card">
  <div class="band" style="left:0;top:150px;width:1100px;height:8px"></div>
  <div class="photo" role="img" aria-label="Photo of a burger and orange juice" style="left:0;top:0;width:200px;height:150px;background:linear-gradient(135deg,#f3b23a,#c9452c)"></div>
  <div class="photo" role="img" aria-label="Photo of boiled eggs and toast" style="left:220px;top:10px;width:200px;height:130px;border-radius:12px;background:radial-gradient(circle,#f4d8a4,#dcb27a)"></div>
  <div class="photo" role="img" aria-label="Photo of fried eggs, toast and hash browns on a plate" style="left:470px;top:5px;width:250px;height:140px;border-radius:50%;background:radial-gradient(circle,#fffaf0,#e8c48a 60%,#d27a2c)"></div>
  <div class="photo" role="img" aria-label="Photo of a toasted sandwich with chips" style="left:860px;top:5px;width:210px;height:140px;border-radius:50%;background:radial-gradient(circle,#d9a45e,#8e5a2c)"></div>

  <div class="brand" style="left:30px;top:180px"><span class="brand-dot"></span>Ward Café</div>
  <div class="food-title section-title" style="left:30px;top:235px">Breakfast Items</div>
  <div class="food-list" style="left:30px;top:265px">
    <div>2 Pieces Raisin Toast $4.0</div>
    <div>Hash Brown $2.0</div>
    <div>Plain Croissant $4.0</div>
    <div>Ham and Cheese Croissant $6.0</div>
    <div>Ham, Cheese and Tomato Toastie $6.50</div>
  </div>

  <div class="food-title section-title" style="left:400px;top:180px">Hot Food and Sandwiches</div>
  <div class="food-list" style="left:400px;top:210px">
    <div>Pre Made Sandwiches $8.50 – $9.50</div>
    <div>Vegetarian Wrap $9.50</div>
    <div>Hot Chips $4.50</div>
    <div>Potato Cakes $2.50</div>
    <div>Dim Sims $2.0</div>
    <div>Pan Hamburger with Chips $12.50</div>
    <div>Chicken Schnitzel Burger $12.50</div>
  </div>
  <div class="small" style="left:780px;top:215px;width:280px;line-height:16px;color:var(--brown)">Please ask at the counter about today's specials and soup of the week</div>
  <div class="small" style="left:780px;top:400px;color:var(--brown)">@wardcafe</div>
</section>

<section class="card coffee-card">
  <div class="brand" style="left:40px;top:40px"><span class="brand-dot"></span>Ward Café</div>
  <div class="hours" style="left:40px;top:95px">Trading Hours: Monday to Friday 6:30 to 4pm</div>
  <div class="photo" role="img" aria-label="Photo of a red takeaway coffee cup with coffee splashing out" style="left:40px;top:250px;width:230px;height:190px;background:linear-gradient(160deg,#5a2a14 0 35%,var(--red) 35%)"></div>

  <div class="photo" role="img" aria-label="Orange brush stroke" style="left:300px;top:30px;width:170px;height:70px;background:linear-gradient(90deg,var(--orange),#f3a456);border-radius:6px"></div>
  <div class="coffee-word" style="left:315px;top:28px">Coffee</div>

  <svg style="position:absolute;left:480px;top:36px" width="16" height="20" viewBox="0 0 16 20" aria-hidden="true"><rect x="2" y="1" width="12" height="18" rx="2" fill="none" stroke="#2a2623" stroke-width="2"/><circle cx="8" cy="15.5" r="1.2" fill="#2a2623"/></svg>
  <div class="small" style="left:502px;top:40px">0400 555 018</div>

  <div class="list" style="left:320px;top:120px">
    <div class="row"><span>Latte</span><span>small $4.0</span><span>Large $4.50</span></div>
    <div class="row"><span>Cappuccino</span><span>small $4.0</span><span>Large $4.50</span></div>
    <div class="row"><span>Flat White</span><span>small $4.0</span><span>Large $4.50</span></div>
    <div class="row"><span>Long Black</span><span>small $4.0</span><span>Large $4.50</span></div>
    <div class="row"><span>Hot Chocolate</span><span>small $4.0</span><span>Large $4.50</span></div>
    <div style="height:14px"></div>
    <div class="row"><span>Chai Latte</span><span>small $4.50</span><span>Large $5.0</span></div>
    <div class="row"><span>Mocha</span><span>small $4.50</span><span>Large $5.0</span></div>
    <div class="row"><span>Dirty Chai</span><span>small $5</span><span>Large $5.50</span></div>
  </div>

  <div class="list" style="left:640px;top:140px;text-align:right;width:160px">
    <div>Espresso $3.50</div>
    <div>Short Macchiato $4.0</div>
    <div>Piccolo $4.0</div>
    <div>Long Macchiato $4.50</div>
  </div>

  <div class="photo" role="img" aria-label="Photo of yoghurt with strawberries and mint in a bowl" style="left:900px;top:20px;width:180px;height:150px;border-radius:50%;background:radial-gradient(circle,#fff 30%,#e33a3a 60%,var(--yellow))"></div>

  <div class="light-title section-title" style="left:640px;top:230px">Something Light:</div>
  <div class="list" style="left:650px;top:268px">
    <div class="row"><span>Mixed Yoghurts</span><span>$5.50</span></div>
    <div class="row"><span>Chia Pudding</span><span>$5.50</span></div>
    <div class="row"><span>Fruit Salad</span><span>$5.50</span></div>
    <div class="row"><span>Bircher Muesli</span><span>$5.50</span></div>
    <div class="row"><span>Protein Balls</span><span>$4.0</span></div>
  </div>
  <div class="list" style="left:860px;top:268px">
    <div class="row"><span>Banana Bread</span><span>$4.50</span></div>
    <div class="row"><span>Muffins</span><span>$4.50</span></div>
    <div class="row"><span>Slices</span><span>$4.0</span></div>
  </div>

  <div class="small" style="left:320px;top:395px;font-size:13px"><b>Extras</b> &nbsp; Soy Milk/Lactose Free Milk/Syrups/Extra Shot/Decaf &nbsp;$0.50 extra</div>
  <div class="small" style="left:960px;top:410px">@wardcafe</div>
</section>

</body>
</html>
```